New Plumbing Company

We are looking for a smart and creative business card design for our new plumbing company. We are looking for creativity and originality in our business cards.

Industry/Entity Type

Plumbing

Contact Information for Business Card

Crestline Plumbing
Peter Halvane
Managing Director
Telephone Number : 0481529604
Email : service@crestlineplumbing.com.au
Website : www.crestlineplumbing.com.au
Lic. 508264K

Colors
0692cd
33a6d7
000000

Requirements
Must have
• I want the business card to be designed on a black background using the blue tones i have selected as seen in the company logo.

```html
<!DOCTYPE html>
<html lang="en">
<head>
<meta charset="utf-8">
<title>Crestline Plumbing – Business Card</title>
<link rel="stylesheet" href="https://fonts.googleapis.com/css2?family=Jost:wght@400;700&display=swap">
<style>
  :root {
    --page: #ffffff;
    --band-1: #171819;
    --band-2: #1b222b;
    --band-3: #1f2d3f;
    --band-4: #233a55;
    --band-5: #27486b;
    --band-6: #295c93;
    --band-7: #2b74c4;
    --band-8: #2a8af0;
    --accent: #2a8af0;
    --text: #ffffff;
  }
  html, body {
    margin: 0;
    padding: 0;
    width: 1200px;
    height: 1000px;
    overflow: hidden;
    background: var(--page);
    font-family: "Jost", "Futura", sans-serif;
  }
  .business-card {
    position: absolute;
    left: 243px;
    top: 291px;
    width: 713px;
    height: 418px;
    overflow: hidden;
    display: flex;
    flex-direction: column;
  }
  .band { width: 100%; flex: 0 0 auto; }
  .band-1 { height: 54px; background: var(--band-1); }
  .band-2 { height: 55px; background: var(--band-2); }
  .band-3 { height: 55px; background: var(--band-3); }
  .band-4 { height: 55px; background: var(--band-4); }
  .band-5 { height: 54px; background: var(--band-5); }
  .band-6 { height: 55px; background: var(--band-6); }
  .band-7 { height: 54px; background: var(--band-7); }
  .band-8 { flex: 1 1 auto; background: var(--band-8); }

  .brand {
    position: absolute;
    left: 0;
    right: 0;
    top: 92px;
    display: flex;
    align-items: center;
    justify-content: center;
    gap: 22px;
  }
  .brand-mark {
    width: 70px;
    height: 70px;
    border: 5px solid var(--accent);
    border-radius: 50%;
    box-sizing: border-box;
  }
  .brand-name {
    color: var(--text);
    font-weight: 400;
    font-size: 44px;
    letter-spacing: 0.5px;
    line-height: 1;
  }

  .person {
    position: absolute;
    left: 60px;
    top: 262px;
    color: var(--text);
    line-height: 27px;
  }
  .person-name { font-weight: 700; font-size: 23px; letter-spacing: 0.3px; }
  .person-role { font-weight: 400; font-size: 21px; }

  .divider {
    position: absolute;
    left: 268px;
    top: 266px;
    width: 2px;
    height: 103px;
    background: var(--text);
  }

  .contact {
    position: absolute;
    left: 311px;
    top: 264px;
    margin: 0;
    padding: 0;
    list-style: none;
    color: var(--text);
    font-size: 21px;
    line-height: 26.5px;
  }
  .contact-label { font-weight: 700; }
</style>
</head>
<body>
  <div class="business-card">
    <div class="band band-1"></div>
    <div class="band band-2"></div>
    <div class="band band-3"></div>
    <div class="band band-4"></div>
    <div class="band band-5"></div>
    <div class="band band-6"></div>
    <div class="band band-7"></div>
    <div class="band band-8"></div>

    <div class="brand">
      <div class="brand-mark"></div>
      <div class="brand-name">Crestline Plumbing</div>
    </div>

    <div class="person">
      <div class="person-name">Peter Halvane</div>
      <div class="person-role">Managing Director</div>
    </div>

    <div class="divider"></div>

    <ul class="contact">
      <li><span class="contact-label">T</span> : 0481529604</li>
      <li><span class="contact-label">E</span> : service@crestlineplumbing.com.au</li>
      <li>www.crestlineplumbing.com.au</li>
      <li>Lic. 508264K</li>
    </ul>
  </div>
</body>
</html>
```